Tide Puffs. the aim is to sell vaping liquids based on mood or feelings

We are a company who sell vaping liquids. A designer from this site created a good logo for our company. I now need to use this logo and create a label to place onto vaping bottles. Unusually we will be selling vaping products based on Moods rather than flavours.

To be clear therefore the label should have our company Logo but then also reflect a particular type of Mood or feeling.

The designs for the various moods will then be printed as labels for our vaping bottles. We have 9 different Tide Puffs (see below) that we intend to bring to the market and general public

i would therfore like designs for the following 9 feelings/moods:

Love
Chilled
Happy
Energy
Desire
Bliss
Lust
Calm
High

the first attachment has our stand alone Logo.

i will then send some attachments of ideas we were playing around with to point you in the right direction. i will need the designs to be very colourful and to reflect the mood.

i do like the love hart one so it doesn't necessarily mean that we need to have images of people on the label. i will leave it to the designers to use images they feel best reflects the specific mood

Target Market(s)

General public

Industry/Entity Type

Retail

Colors

Designer to choose colors to be used in the design.

Requirements
Must have
• my company logo on any design
Nice to have
• vibrant colours or image to match the particular mood vape

```html
<!DOCTYPE html>
<html lang="en">
<head>
<meta charset="utf-8">
<title>Tide Puffs – Feeling Labels</title>
<link rel="stylesheet" href="https://fonts.googleapis.com/css2?family=Bungee&family=Montserrat:wght@600;700;800&family=Lobster&display=swap">
<style>
  :root{
    --page:#ffffff;
    --ink:#ffffff;
    --warn-red:#e0262b;
    --gold-1:#f6d86a;
    --gold-2:#b98a1c;
    --paint:linear-gradient(120deg,#ff3b3b 0%,#ffd23a 18%,#3ddc5a 34%,#2ab3ff 50%,#ff4fd8 66%,#ffd23a 82%,#ff3b3b 100%);
  }
  *{box-sizing:border-box;margin:0;padding:0}
  html,body{width:1200px;height:936px;overflow:hidden;background:var(--page)}
  .sheet{
    position:relative;width:1200px;height:936px;
    display:grid;grid-template-columns:repeat(3,362px);grid-template-rows:repeat(3,260px);
    column-gap:29px;row-gap:41px;padding:30px 29px 0 29px;
  }
  .label{position:relative;overflow:hidden;background:var(--bg);font-family:"Montserrat",sans-serif;color:var(--ink)}
  .label__photo{position:absolute}
  .label__photo--left{left:0;top:0;width:140px;height:150px;background:radial-gradient(ellipse at 45% 40%,var(--photo-a) 0%,transparent 70%)}
  .label__photo--right{right:0;top:0;width:150px;height:260px;background:radial-gradient(ellipse at 60% 45%,var(--photo-b) 0%,transparent 72%)}
  .label__frame{position:absolute;inset:4px;border:2px solid var(--edge)}
  .label__brand{
    position:absolute;left:104px;top:50px;width:150px;text-align:center;
    font-family:"Montserrat",sans-serif;font-weight:800;font-size:25px;line-height:1;color:var(--brand);
  }
  .label__specs{position:absolute;left:24px;top:118px;font-size:9px;font-weight:700;line-height:10px}
  .label__icons{position:absolute;left:21px;top:143px;width:74px;height:50px;background:rgba(0,0,0,.35)}
  .label__warning{position:absolute;left:22px;top:200px;width:92px;font-size:3.6px;line-height:4.5px;color:rgba(255,255,255,.8)}
  .label__warning strong{display:block;font-size:5px;line-height:6px;color:#fff}
  .label__feeling{
    position:absolute;left:122px;top:112px;white-space:nowrap;
    font-family:"Bungee",sans-serif;font-size:62px;line-height:58px;letter-spacing:-3px;
    background:var(--paint);-webkit-background-clip:text;background-clip:text;color:transparent;
  }
  .label__feeling--wide{font-size:50px;line-height:58px;left:118px;letter-spacing:-2px}
  .label__feeling--long{font-size:44px;line-height:58px;left:116px;letter-spacing:-2px}
  .label__badge{
    position:absolute;left:287px;top:186px;width:52px;height:52px;border-radius:50%;
    background:radial-gradient(circle at 40% 35%,var(--badge-1),var(--badge-2));
    box-shadow:inset 0 0 0 4px rgba(255,255,255,.35),inset 0 0 0 13px rgba(0,0,0,.12);
  }
  .label__stamp{
    position:absolute;right:30px;top:18px;width:54px;padding:2px 0;border:1px solid #fff;border-radius:4px;
    font-family:"Lobster",cursive;font-size:9px;line-height:9px;text-align:center;color:#fff;
  }

  .label--happy{--bg:linear-gradient(110deg,#3a1c5a 0%,#2a2f8a 35%,#6a1f7a 60%,#1f8a3a 100%);--photo-a:#b9b0c8;--photo-b:#e3e3ee;--edge:#5fd4e6;--brand:#ff4fa8;--badge-1:var(--gold-1);--badge-2:var(--gold-2)}
  .label--lust{--bg:linear-gradient(110deg,#6a0b0f 0%,#b0141a 45%,#d4561a 100%);--photo-a:#d63a3a;--photo-b:#e04a2a;--edge:#e3262b;--brand:#ff4fa8;--badge-1:#ffb08a;--badge-2:#d8421c}
  .label--high{--bg:linear-gradient(110deg,#063a3a 0%,#0b6a6a 50%,#0f8f8f 100%);--photo-a:#3aa7a7;--photo-b:#5cc8c8;--edge:#e6b43a;--brand:#ff4fa8;--badge-1:#7fe6f0;--badge-2:#1a9fb0}
  .label--energy{--bg:linear-gradient(110deg,#3a1a0a 0%,#7a3c10 45%,#e0901a 100%);--photo-a:#8a5a3a;--photo-b:#f0a82a;--edge:#f2b31a;--brand:#ff4fa8;--badge-1:var(--gold-1);--badge-2:var(--gold-2)}
  .label--chilled{--bg:linear-gradient(110deg,#0b2a6a 0%,#1a3e9a 50%,#22306a 100%);--photo-a:#6a8ad0;--photo-b:#8aa0d8;--edge:#2a5ad8;--brand:#ff4fa8;--badge-1:#f2f2f6;--badge-2:#9aa0b8}
  .label--desire{--bg:linear-gradient(110deg,#4a0a1a 0%,#7a1a2a 50%,#c0561a 100%);--photo-a:#b04a5a;--photo-b:#d8823a;--edge:#d42a2a;--brand:#ff4fa8;--badge-1:var(--gold-1);--badge-2:var(--gold-2)}
  .label--calm{--bg:linear-gradient(110deg,#3a0f5a 0%,#6a2a9a 50%,#8a3aa8 100%);--photo-a:#b08ad0;--photo-b:#c9a8e0;--edge:#a64ad0;--brand:#ff4fa8;--badge-1:var(--gold-1);--badge-2:var(--gold-2)}
  .label--bliss{--bg:linear-gradient(110deg,#0a3a0f 0%,#1a7a1f 50%,#3aa02a 100%);--photo-a:#5a9a5a;--photo-b:#7ac05a;--edge:#c8d62a;--brand:#ff4fa8;--badge-1:var(--gold-1);--badge-2:var(--gold-2)}
  .label--love{--bg:linear-gradient(110deg,#3a0f3a 0%,#8a1a6a 50%,#d42a7a 100%);--photo-a:#8a4a8a;--photo-b:#ff3a5a;--edge:#e23a8a;--brand:#ff4fa8;--badge-1:var(--gold-1);--badge-2:var(--gold-2)}
</style>
</head>
<body>
<main class="sheet">

  <section class="label label--happy">
    <div class="label__photo label__photo--left" role="img" aria-label="Photo of a woman exhaling vapour"></div>
    <div class="label__photo label__photo--right" role="img" aria-label="Colourful swirling smoke"></div>
    <div class="label__frame"></div>
    <p class="label__brand">Tide Puffs</p>
    <p class="label__specs">VG: 70<br>PG: 30</p>
    <svg class="label__icons" viewBox="0 0 74 50" aria-hidden="true"><g fill="none" stroke="var(--warn-red)" stroke-width="2"><circle cx="20" cy="14" r="7"/><path d="M47 8 L54 20 L40 20 Z"/><circle cx="20" cy="37" r="7"/><circle cx="47" cy="37" r="7"/></g><g fill="#fff"><rect x="47" y="11" width="1.5" height="5"/><rect x="17" y="34" width="6" height="6"/><rect x="44" y="34" width="6" height="6"/></g></svg>
    <p class="label__warning"><strong>WARNING</strong>This liquid contains nicotine which is a highly addictive substance. Keep away from children and pets. Not for sale to anyone under the age of 18.</p>
    <p class="label__feeling">HA<br>PPY</p>
    <div class="label__badge" role="img" aria-label="Quality seal"></div>
  </section>

  <section class="label label--lust">
    <div class="label__photo label__photo--left" role="img" aria-label="Photo of two women in red light"></div>
    <div class="label__photo label__photo--right" role="img" aria-label="Photo of legs in high heels"></div>
    <div class="label__frame"></div>
    <p class="label__stamp">Premium<br>Vape liquid</p>
    <p class="label__brand">Tide Puffs</p>
    <p class="label__specs">VG: 70<br>PG: 30</p>
    <svg class="label__icons" viewBox="0 0 74 50" aria-hidden="true"><g fill="none" stroke="var(--warn-red)" stroke-width="2"><circle cx="20" cy="14" r="7"/><path d="M47 8 L54 20 L40 20 Z"/><circle cx="20" cy="37" r="7"/><circle cx="47" cy="37" r="7"/></g><g fill="#fff"><rect x="47" y="11" width="1.5" height="5"/><rect x="17" y="34" width="6" height="6"/><rect x="44" y="34" width="6" height="6"/></g></svg>
    <p class="label__warning"><strong>WARNING</strong>This liquid contains nicotine which is a highly addictive substance. Keep away from children and pets. Not for sale to anyone under the age of 18.</p>
    <p class="label__feeling">LU<br>ST</p>
    <div class="label__badge" role="img" aria-label="Quality seal"></div>
  </section>

  <section class="label label--high">
    <div class="label__photo label__photo--left" role="img" aria-label="Photo of a woman vaping in teal light"></div>
    <div class="label__photo label__photo--right" role="img" aria-label="Photo of a woman exhaling vapour"></div>
    <div class="label__frame"></div>
    <p class="label__brand">Tide Puffs</p>
    <p class="label__specs">VG: 70<br>PG: 30</p>
    <svg class="label__icons" viewBox="0 0 74 50" aria-hidden="true"><g fill="none" stroke="var(--warn-red)" stroke-width="2"><circle cx="20" cy="14" r="7"/><path d="M47 8 L54 20 L40 20 Z"/><circle cx="20" cy="37" r="7"/><circle cx="47" cy="37" r="7"/></g><g fill="#fff"><rect x="47" y="11" width="1.5" height="5"/><rect x="17" y="34" width="6" height="6"/><rect x="44" y="34" width="6" height="6"/></g></svg>
    <p class="label__warning"><strong>WARNING</strong>This liquid contains nicotine which is a highly addictive substance. Keep away from children and pets. Not for sale to anyone under the age of 18.</p>
    <p class="label__feeling">HI<br>GH</p>
    <div class="label__badge" role="img" aria-label="Quality seal"></div>
  </section>

  <section class="label label--energy">
    <div class="label__photo label__photo--left" role="img" aria-label="Photo of a dancer in motion"></div>
    <div class="label__photo label__photo--right" role="img" aria-label="Photo of a breakdancer with light trails"></div>
    <div class="label__frame"></div>
    <p class="label__brand">Tide Puffs</p>
    <p class="label__specs">VG: 70<br>PG: 30</p>
    <svg class="label__icons" viewBox="0 0 74 50" aria-hidden="true"><g fill="none" stroke="var(--warn-red)" stroke-width="2"><circle cx="20" cy="14" r="7"/><path d="M47 8 L54 20 L40 20 Z"/><circle cx="20" cy="37" r="7"/><circle cx="47" cy="37" r="7"/></g><g fill="#fff"><rect x="47" y="11" width="1.5" height="5"/><rect x="17" y="34" width="6" height="6"/><rect x="44" y="34" width="6" height="6"/></g></svg>
    <p class="label__warning"><strong>WARNING</strong>This liquid contains nicotine which is a highly addictive substance. Keep away from children and pets. Not for sale to anyone under the age of 18.</p>
    <p class="label__feeling label__feeling--wide">ENE<br>RGY</p>
    <div class="label__badge" role="img" aria-label="Quality seal"></div>
  </section>

  <section class="label label--chilled">
    <div class="label__photo label__photo--left" role="img" aria-label="Photo of a frosty winter forest with icicles"></div>
    <div class="label__photo label__photo--right" role="img" aria-label="Photo of a woman exhaling cold vapour"></div>
    <div class="label__frame"></div>
    <p class="label__brand">Tide Puffs</p>
    <p class="label__specs">VG: 70<br>PG: 30</p>
    <svg class="label__icons" viewBox="0 0 74 50" aria-hidden="true"><g fill="none" stroke="var(--warn-red)" stroke-width="2"><circle cx="20" cy="14" r="7"/><path d="M47 8 L54 20 L40 20 Z"/><circle cx="20" cy="37" r="7"/><circle cx="47" cy="37" r="7"/></g><g fill="#fff"><rect x="47" y="11" width="1.5" height="5"/><rect x="17" y="34" width="6" height="6"/><rect x="44" y="34" width="6" height="6"/></g></svg>
    <p class="label__warning"><strong>WARNING</strong>This liquid contains nicotine which is a highly addictive substance. Keep away from children and pets. Not for sale to anyone under the age of 18.</p>
    <p class="label__feeling label__feeling--long">CHI<br>LLED</p>
    <div class="label__badge" role="img" aria-label="Quality seal"></div>
  </section>

  <section class="label label--desire">
    <div class="label__photo label__photo--left" role="img" aria-label="Close-up photo of lips"></div>
    <div class="label__photo label__photo--right" role="img" aria-label="Photo of a reclining woman in warm light"></div>
    <div class="label__frame"></div>
    <p class="label__stamp">Premium<br>Vape liquid</p>
    <p class="label__brand">Tide Puffs</p>
    <p class="label__specs">VG: 70<br>PG: 30</p>
    <svg class="label__icons" viewBox="0 0 74 50" aria-hidden="true"><g fill="none" stroke="var(--warn-red)" stroke-width="2"><circle cx="20" cy="14" r="7"/><path d="M47 8 L54 20 L40 20 Z"/><circle cx="20" cy="37" r="7"/><circle cx="47" cy="37" r="7"/></g><g fill="#fff"><rect x="47" y="11" width="1.5" height="5"/><rect x="17" y="34" width="6" height="6"/><rect x="44" y="34" width="6" height="6"/></g></svg>
    <p class="label__warning"><strong>WARNING</strong>This liquid contains nicotine which is a highly addictive substance. Keep away from children and pets. Not for sale to anyone under the age of 18.</p>
    <p class="label__feeling label__feeling--wide">DES<br>IRE</p>
    <div class="label__badge" role="img" aria-label="Quality seal"></div>
  </section>

  <section class="label label--calm">
    <div class="label__photo label__photo--left" role="img" aria-label="Photo of a woman meditating"></div>
    <div class="label__photo label__photo--right" role="img" aria-label="Photo of a woman blowing vapour rings"></div>
    <div class="label__frame"></div>
    <p class="label__brand">Tide Puffs</p>
    <p class="label__specs">VG: 70<br>PG: 30</p>
    <svg class="label__icons" viewBox="0 0 74 50" aria-hidden="true"><g fill="none" stroke="var(--warn-red)" stroke-width="2"><circle cx="20" cy="14" r="7"/><path d="M47 8 L54 20 L40 20 Z"/><circle cx="20" cy="37" r="7"/><circle cx="47" cy="37" r="7"/></g><g fill="#fff"><rect x="47" y="11" width="1.5" height="5"/><rect x="17" y="34" width="6" height="6"/><rect x="44" y="34" width="6" height="6"/></g></svg>
    <p class="label__warning"><strong>WARNING</strong>This liquid contains nicotine which is a highly addictive substance. Keep away from children and pets. Not for sale to anyone under the age of 18.</p>
    <p class="label__feeling">CA<br>LM</p>
    <div class="label__badge" role="img" aria-label="Quality seal"></div>
  </section>

  <section class="label label--bliss">
    <div class="label__photo label__photo--left" role="img" aria-label="Photo of a woman in a hat in green light"></div>
    <div class="label__photo label__photo--right" role="img" aria-label="Photo of a woman vaping beside a clock"></div>
    <div class="label__frame"></div>
    <p class="label__stamp">Premium<br>Vape liquid</p>
    <p class="label__brand">Tide Puffs</p>
    <p class="label__specs">VG: 70<br>PG: 30</p>
    <svg class="label__icons" viewBox="0 0 74 50" aria-hidden="true"><g fill="none" stroke="var(--warn-red)" stroke-width="2"><circle cx="20" cy="14" r="7"/><path d="M47 8 L54 20 L40 20 Z"/><circle cx="20" cy="37" r="7"/><circle cx="47" cy="37" r="7"/></g><g fill="#fff"><rect x="47" y="11" width="1.5" height="5"/><rect x="17" y="34" width="6" height="6"/><rect x="44" y="34" width="6" height="6"/></g></svg>
    <p class="label__warning"><strong>WARNING</strong>This liquid contains nicotine which is a highly addictive substance. Keep away from children and pets. Not for sale to anyone under the age of 18.</p>
    <p class="label__feeling label__feeling--wide">BLI<br>SS</p>
    <div class="label__badge" role="img" aria-label="Quality seal"></div>
  </section>

  <section class="label label--love">
    <div class="label__photo label__photo--left" role="img" aria-label="Photo of an embracing couple"></div>
    <div class="label__photo label__photo--right" role="img" aria-label="Glowing red hearts"></div>
    <div class="label__frame"></div>
    <p class="label__brand">Tide Puffs</p>
    <p class="label__specs">VG: 70<br>PG: 30</p>
    <svg class="label__icons" viewBox="0 0 74 50" aria-hidden="true"><g fill="none" stroke="var(--warn-red)" stroke-width="2"><circle cx="20" cy="14" r="7"/><path d="M47 8 L54 20 L40 20 Z"/><circle cx="20" cy="37" r="7"/><circle cx="47" cy="37" r="7"/></g><g fill="#fff"><rect x="47" y="11" width="1.5" height="5"/><rect x="17" y="34" width="6" height="6"/><rect x="44" y="34" width="6" height="6"/></g></svg>
    <p class="label__warning"><strong>WARNING</strong>This liquid contains nicotine which is a highly addictive substance. Keep away from children and pets. Not for sale to anyone under the age of 18.</p>
    <p class="label__feeling">LO<br>VE</p>
    <div class="label__badge" role="img" aria-label="Quality seal"></div>
  </section>

</main>
</body>
</html>
```